Realty Group Needs Classy, Contemporary Letterhead Design

We need a letterhead design for a new realty company located in NY, USA. We buy investment properties to rehabilitate and or keep in our rental portfolio.

```html
<!DOCTYPE html>
<html lang="en">
<head>
<meta charset="utf-8">
<title>Meridian Realty Group – Letterhead</title>
<link href="https://fonts.googleapis.com/css2?family=EB+Garamond:ital,wght@0,400;1,400&family=Open+Sans:wght@400;700&display=swap" rel="stylesheet">
<style>
  :root {
    --backdrop: #ffffff;
    --paper: #f1f1f1;
    --brand-purple: #5f4a8b;
    --band-grey: #8a8a8a;
    --ink: #4a4a4a;
    --ink-soft: #5a5a5a;
    --on-band: #ffffff;
  }
  * { margin: 0; padding: 0; box-sizing: border-box; }
  html, body {
    width: 1200px; height: 803px; overflow: hidden;
    background: var(--backdrop);
  }
  .letterhead {
    position: absolute; left: 397px; top: 125px;
    width: 409px; height: 575px;
    background: var(--paper);
    font-family: "EB Garamond", Georgia, serif;
    color: var(--ink);
  }
  .brand {
    position: absolute; top: 48px; left: 0; width: 100%;
    text-align: center; color: var(--brand-purple);
    font-family: "Open Sans", Arial, sans-serif; font-weight: 700;
  }
  .brand-name { font-size: 30px; letter-spacing: -0.5px; line-height: 1; }
  .brand-sub { font-size: 10.5px; letter-spacing: 0.4px; margin-top: 2px; }
  .recipient {
    position: absolute; left: 21px; top: 108px;
    font-size: 7.6px; line-height: 10px;
  }
  .recipient .name { font-style: italic; }
  .date {
    position: absolute; right: 21px; top: 108px;
    font-family: "Open Sans", Arial, sans-serif; font-size: 7px;
  }
  .body-copy {
    position: absolute; left: 21px; top: 174px; width: 368px;
    font-size: 6.9px; line-height: 9.2px; text-align: justify;
    color: var(--ink-soft);
  }
  .body-copy p { margin-bottom: 9px; }
  .signature {
    position: absolute; left: 21px; top: 416px;
    font-size: 7.6px; line-height: 10px;
  }
  .footer { position: absolute; left: 0; top: 508px; width: 409px; height: 42px; }
  .footer svg.bands { position: absolute; inset: 0; }
  .contact {
    position: absolute; display: flex; align-items: center; gap: 9px;
    font-family: "Open Sans", Arial, sans-serif; font-size: 7.6px;
    color: var(--on-band); white-space: nowrap;
  }
  .contact svg { width: 8px; height: 8px; fill: none; stroke: var(--on-band); stroke-width: 1.3; }
</style>
</head>
<body>
  <main class="letterhead">
    <header class="brand">
      <div class="brand-name">MERIDIAN</div>
      <div class="brand-sub">Realty Group, LLC</div>
    </header>

    <address class="recipient" style="font-style:normal">
      <div class="name">Mr. Name Here</div>
      <div>Insert Company Name</div>
      <div>Insert Address Here</div>
      <div>City, State 00000</div>
    </address>
    <div class="date">December 28, 2021</div>

    <section class="body-copy">
      <p>Lorem ipsum dolor sit amet, consectetur adipiscing elit. Integer nec odio. Praesent libero. Sed cursus ante dapibus diam. Sed nisi. Nulla quis sem at nibh elementum imperdiet. Duis sagittis ipsum. Praesent mauris. Fusce nec tellus sed augue semper porta.</p>
      <p>Curabitur tortor. Pellentesque nibh. Aenean quam. In scelerisque sem at dolor. Maecenas mattis. Sed convallis tristique sem. Proin ut ligula vel nunc egestas porttitor. Morbi lectus risus, iaculis vel, suscipit quis, luctus non, massa. Fusce ac turpis quis ligula lacinia aliquet. Mauris ipsum. Nulla metus metus, ullamcorper vel, tincidunt sed, euismod in nibh.</p>
      <p>Class aptent taciti sociosqu ad litora torquent per conubia nostra, per inceptos himenaeos. Nam nec ante. Sed lacinia, urna non tincidunt mattis, tortor neque adipiscing diam, a cursus ipsum ante quis turpis. Nulla facilisi. Ut fringilla. Suspendisse potenti. Nunc feugiat mi a tellus consequat imperdiet. Vestibulum sapien. Proin quam. Etiam ultrices. Suspendisse in justo eu magna luctus suscipit.</p>
      <p>Sed lectus. Integer euismod lacus luctus magna. Quisque cursus, metus vitae pharetra auctor, sem massa mattis sem, at interdum magna augue eget diam. Vestibulum ante ipsum primis in faucibus orci luctus et ultrices posuere cubilia Curae; Morbi lacinia molestie dui. Praesent blandit dolor. Sed non quam. In vel mi sit amet augue congue elementum. Morbi in ipsum sit amet pede facilisis laoreet. Donec lacus nunc, viverra nec, blandit vel, egestas et, augue. Vestibulum tincidunt malesuada tellus. Ut ultrices ultrices enim. Curabitur sit amet mauris. Morbi in dui quis est pulvinar ullamcorper.</p>
      <p>Thank you for being one of our valued customers.</p>
    </section>

    <div class="signature">
      <div>Name Here</div>
      <div>CEO</div>
    </div>

    <footer class="footer">
      <svg class="bands" viewBox="0 0 409 42" width="409" height="42">
        <polygon points="0,0 233,0 262,42 0,42" fill="var(--brand-purple)"/>
        <polygon points="251,17 409,17 409,42 273,42" fill="var(--band-grey)"/>
      </svg>

      <div class="contact" style="left:18px; top:9px">
        <svg viewBox="0 0 10 10"><path d="M2 1 L4 1 L4.8 3.2 L3.6 4 Q4.6 6 6 6.4 L6.8 5.2 L9 6 L9 8 Q5 9 2.2 5.8 Q0.8 3.6 2 1 Z"/></svg>
        <span>+1.234.567.89.00</span>
      </div>
      <div class="contact" style="left:18px; top:21px">
        <svg viewBox="0 0 10 10"><rect x="1" y="4" width="8" height="5" rx="1"/><path d="M1.5 4 Q5 0.5 8.5 4"/></svg>
        <span>+1.234.567.89.00</span>
      </div>
      <div class="contact" style="left:119px; top:9px">
        <svg viewBox="0 0 10 10"><circle cx="5" cy="5" r="4"/><ellipse cx="5" cy="5" rx="1.8" ry="4"/><path d="M1 5 H9"/></svg>
        <span>www.yourwebsite.com</span>
      </div>
      <div class="contact" style="left:119px; top:21px">
        <svg viewBox="0 0 10 10"><rect x="1" y="2" width="8" height="6"/><path d="M1 2 L5 5.5 L9 2"/></svg>
        <span>yourname@mailbox.com</span>
      </div>
      <div class="contact" style="left:299px; top:25px">
        <svg viewBox="0 0 10 10"><path d="M5 9.5 Q1.5 5.5 1.5 3.8 A3.5 3.5 0 0 1 8.5 3.8 Q8.5 5.5 5 9.5 Z"/><circle cx="5" cy="3.8" r="1.2"/></svg>
        <span>Your Address, location</span>
      </div>
    </footer>
  </main>
</body>
</html>
```